Business Card Re-Design/Update

We'd like to update out business cards. I've included our current "Style guide" which has the colour scheme of the organisation in it. I've also included the branding files with logos etc in them.

I've also included a copy of one of our existing cards so that you can see how ugly/dated they look. I'd like a fresh modern corporate look.

Target Market(s)

These are for our clients, potential clients, industry contacts - like all business cards

Contact Information for Business Card

Name
Position
Company Address - Level 1, 47 Garnet Lane, Toowong Qld 4066
Direct Phone
mobile
Email
Website -www.korvalnet.com.au
Logo

Colors

Designer to choose colors to be used in the design.

Requirements
Must have
• Main Logo
• Cards will need to be editable to be able to personalize them for each new employee.
Nice to have
• The MapOUT, HandOVER, UpKEEP would be okay to have if they can be sensibly and professionally added to the look without detracting from the main imagery.
• Maybe they could go on the back of the card? will leave this to your creative discretion as to whether/where they fit.
Should not have
• Should not have decorative or script fonts

```html
<!DOCTYPE html>
<html lang="en">
<head>
<meta charset="utf-8">
<title>Korvalnet Business Card</title>
<link rel="stylesheet" href="https://fonts.googleapis.com/css2?family=Montserrat:wght@400;500;600&family=Roboto+Condensed:wght@700&display=swap">
<style>
  :root {
    --brand-red: #d71f26;
    --ink: #3a3a3c;
    --ink-soft: #555558;
    --card: #ffffff;
    --tint: #f8dde1;
    --stage: #2b2b2b;
  }
  * { box-sizing: border-box; margin: 0; padding: 0; }
  html, body { width: 1200px; height: 1200px; overflow: hidden; }
  body {
    background: var(--stage);
    font-family: "Montserrat", sans-serif;
    color: var(--ink);
    position: relative;
  }
  .card {
    position: absolute;
    left: 160px;
    width: 880px;
    height: 538px;
    background: var(--card);
    overflow: hidden;
    box-shadow: 0 10px 30px rgba(0,0,0,.35);
  }
  .card--front { top: 31px; }
  .card--back { top: 631px; }

  .pattern-area {
    position: absolute;
    inset: 0;
  }
  .card--front .pattern-area {
    background: linear-gradient(200deg, rgba(248,221,225,.9) 0%, rgba(248,221,225,.35) 45%, rgba(255,255,255,0) 70%);
  }
  .card--back .pattern-area {
    background: linear-gradient(20deg, rgba(248,221,225,.9) 0%, rgba(248,221,225,.35) 45%, rgba(255,255,255,0) 72%);
  }

  .brand {
    position: absolute;
    display: flex;
    align-items: center;
    gap: 16px;
  }
  .brand__mark {
    width: 34px;
    height: 34px;
    background: var(--brand-red);
  }
  .brand__name {
    font-weight: 600;
    color: var(--ink);
    letter-spacing: -0.5px;
    line-height: 1;
  }
  .card--front .brand { left: 56px; top: 60px; }
  .card--front .brand__name { font-size: 54px; }

  .person {
    position: absolute;
    right: 56px;
    top: 128px;
    text-align: right;
  }
  .person__name {
    font-size: 34px;
    font-weight: 500;
    color: var(--brand-red);
  }
  .person__role {
    font-size: 18px;
    color: var(--ink-soft);
    margin-top: 4px;
  }
  .name-tab {
    position: absolute;
    right: 0;
    top: 130px;
    width: 30px;
    height: 46px;
    background: var(--brand-red);
  }

  .contact {
    position: absolute;
    left: 64px;
    top: 252px;
    font-size: 17px;
    line-height: 1.3;
    color: var(--ink);
  }
  .contact__group { margin-bottom: 20px; }
  .contact__label {
    display: inline-block;
    width: 22px;
    font-weight: 600;
    color: var(--brand-red);
  }

  .card--back .brand {
    left: 50%;
    top: 170px;
    transform: translateX(-50%);
  }
  .card--back .brand__mark { width: 44px; height: 44px; }
  .card--back .brand__name { font-size: 66px; }

  .services {
    position: absolute;
    left: 0;
    right: 0;
    top: 282px;
    display: flex;
    justify-content: center;
    gap: 18px;
  }
  .service {
    width: 122px;
    height: 122px;
    position: relative;
  }
  .service::before {
    content: "";
    position: absolute;
    inset: 18px;
    background: var(--brand-red);
    transform: rotate(45deg);
  }
  .service__label {
    position: absolute;
    inset: 0;
    display: flex;
    align-items: center;
    justify-content: center;
    text-align: center;
    font-family: "Roboto Condensed", sans-serif;
    font-weight: 700;
    font-size: 18px;
    line-height: 1.1;
    color: #fff;
  }

  .web-line {
    position: absolute;
    left: 0;
    right: 0;
    top: 448px;
    display: flex;
    align-items: center;
    gap: 22px;
  }
  .web-line__rule {
    flex: 1;
    height: 2px;
    background: var(--brand-red);
  }
  .web-line__url {
    font-size: 18px;
    letter-spacing: 7px;
    color: var(--brand-red);
  }
</style>
</head>
<body>

  <section class="card card--front">
    <div class="pattern-area" role="img" aria-label="Soft pink geometric triangle pattern"></div>

    <div class="brand">
      <span class="brand__mark"></span>
      <span class="brand__name">korvalnet</span>
    </div>

    <div class="name-tab"></div>
    <div class="person">
      <p class="person__name">Maya Delaney</p>
      <p class="person__role">Business Development Manager</p>
    </div>

    <div class="contact">
      <div class="contact__group">
        <p>Level 1, 47 Garnet Lane</p>
        <p>Toowong Qld 4066</p>
      </div>
      <div class="contact__group">
        <p><span class="contact__label">M</span>+61 (0)412 555 208</p>
        <p><span class="contact__label">P</span>+61 (0)7 3000 4127</p>
      </div>
      <div class="contact__group">
        <p><span class="contact__label">D</span>+61 (0)7 3000 4130</p>
        <p><span class="contact__label">F</span>+61 (0)7 3000 4139</p>
      </div>
      <div class="contact__group">
        <p><span class="contact__label">E</span>mdelaney@korvalnet.com.au</p>
      </div>
    </div>
  </section>

  <section class="card card--back">
    <div class="pattern-area" role="img" aria-label="Soft pink geometric triangle pattern"></div>

    <div class="brand">
      <span class="brand__mark"></span>
      <span class="brand__name">korvalnet</span>
    </div>

    <div class="services">
      <div class="service"><span class="service__label">The<br>MapOUT</span></div>
      <div class="service"><span class="service__label">HandOVER</span></div>
      <div class="service"><span class="service__label">UpKEEP</span></div>
    </div>

    <div class="web-line">
      <span class="web-line__rule"></span>
      <span class="web-line__url">www.korvalnet.com.au</span>
      <span class="web-line__rule"></span>
    </div>
  </section>

</body>
</html>
```